KJ Glimmer Cleaning Business Card

We need a business card for our new business, a cleaning company using steam. We already have a logo, and would like a modern-looking card using colors that go well with those in our logo.

```html
<!DOCTYPE html>
<html lang="en">
<head>
<meta charset="utf-8">
<title>KJ Glimmer Cleaning – Business Card</title>
<link href="https://fonts.googleapis.com/css2?family=Lato:wght@300;400;700;900&display=swap" rel="stylesheet">
<style>
  :root {
    --bg: #e4e5e6;
    --green-dark: #1f5d1f;
    --green-mid: #2f8a2b;
    --green-bright: #5aa82a;
    --green-lime: #b7d62a;
    --white: #ffffff;
    --brand-blue: #2a6cc8;
    --text-light: #ffffff;
  }
  * { box-sizing: border-box; margin: 0; padding: 0; }
  html, body { width: 1200px; height: 926px; overflow: hidden; }
  body {
    background: var(--bg);
    font-family: "Lato", sans-serif;
    position: relative;
  }
  .card {
    position: absolute;
    left: 250px;
    width: 700px;
    height: 400px;
    overflow: hidden;
    box-shadow: 0 6px 18px rgba(0,0,0,0.25);
  }
  .card--front { top: 50px; background: var(--green-mid); }
  .card--back { top: 476px; }

  /* Front */
  .front-top {
    position: absolute; inset: 0 0 auto 0; height: 95px;
    background: radial-gradient(ellipse at 50% 0%, var(--green-lime) 0%, var(--green-bright) 45%, var(--green-dark) 100%);
  }
  .front-band {
    position: absolute; left: 0; right: 0; top: 95px; height: 140px;
    background: var(--white);
    border-top: 4px solid var(--green-dark);
    border-bottom: 4px solid var(--green-dark);
    display: flex; align-items: center; justify-content: center;
  }
  .front-bottom {
    position: absolute; inset: 235px 0 0 0;
    background: linear-gradient(180deg, var(--green-mid) 0%, var(--green-bright) 45%, var(--green-dark) 100%);
  }
  .brand {
    display: flex; align-items: center; gap: 14px;
  }
  .brand__dot {
    width: 58px; height: 58px; border-radius: 50%;
    background: var(--green-bright);
    flex: none;
  }
  .brand__name {
    font-family: "Lato", sans-serif;
    font-weight: 900;
    color: var(--brand-blue);
    font-size: 38px;
    line-height: 1;
  }

  /* Back */
  .back-bg {
    position: absolute; inset: 0;
    background: radial-gradient(ellipse at 75% 20%, var(--green-bright) 0%, var(--green-mid) 50%, var(--green-dark) 100%);
  }
  .back-shape { position: absolute; inset: 0; }
  .back-pattern {
    position: absolute; left: 390px; top: 0; width: 310px; height: 150px;
    background: radial-gradient(ellipse at 60% 30%, rgba(40,110,35,0.55) 0%, rgba(40,110,35,0) 70%);
  }
  .back-brand {
    position: absolute; left: 60px; top: 150px;
    gap: 12px;
  }
  .back-brand .brand__dot { width: 50px; height: 50px; }
  .back-brand .brand__name { font-size: 26px; line-height: 1.05; }
  .brand__line { display: block; }
  .contact {
    position: absolute; right: 30px; top: 140px;
    text-align: right; color: var(--text-light);
  }
  .contact__name {
    font-size: 38px; font-weight: 300; margin-bottom: 12px;
  }
  .contact__name strong { font-weight: 700; }
  .contact__list { list-style: none; }
  .contact__item {
    display: flex; justify-content: flex-end; align-items: center; gap: 12px;
    font-size: 19px; line-height: 27px;
  }
  .icon { width: 18px; height: 18px; fill: var(--text-light); flex: none; }
  .icon--blank { fill: none; }
</style>
</head>
<body>

<section class="card card--front" aria-label="Business card front">
  <div class="front-top"></div>
  <div class="front-band">
    <div class="brand">
      <span class="brand__dot"></span>
      <span class="brand__name">KJ Glimmer Cleaning</span>
    </div>
  </div>
  <div class="front-bottom"></div>
</section>

<section class="card card--back" aria-label="Business card back">
  <div class="back-bg"></div>
  <div class="back-pattern" role="img" aria-label="Decorative halftone dot pattern in deep green"></div>
  <svg class="back-shape" width="700" height="400" viewBox="0 0 700 400">
    <rect x="0" y="0" width="26" height="400" fill="#2f8a2b"/>
    <path d="M26 0 H320 C370 120 340 290 225 400 H26 Z" fill="#ffffff"/>
  </svg>
  <div class="brand back-brand">
    <span class="brand__dot"></span>
    <span class="brand__name"><span class="brand__line">KJ Glimmer</span><span class="brand__line">Cleaning</span></span>
  </div>
  <div class="contact">
    <p class="contact__name">John <strong>Smith</strong></p>
    <ul class="contact__list">
      <li class="contact__item">123-456-7890
        <svg class="icon" viewBox="0 0 24 24"><path d="M6.6 10.8a15 15 0 0 0 6.6 6.6l2.2-2.2a1 1 0 0 1 1-.25 11.4 11.4 0 0 0 3.6.57 1 1 0 0 1 1 1V20a1 1 0 0 1-1 1A17 17 0 0 1 3 4a1 1 0 0 1 1-1h3.5a1 1 0 0 1 1 1c0 1.25.2 2.45.57 3.57a1 1 0 0 1-.25 1z"/></svg></li>
      <li class="contact__item">yourdomain.com
        <svg class="icon" viewBox="0 0 24 24"><path d="M2 5h20v14H2zm2 2v.5l8 5 8-5V7zm0 2.8V17h16V9.8l-8 5z"/></svg></li>
      <li class="contact__item">yourname@yourdomain.com
        <svg class="icon" viewBox="0 0 24 24"><path d="M12 2a10 10 0 1 0 0 20 10 10 0 0 0 0-20zm6.9 6h-3a15 15 0 0 0-1.3-3.6A8 8 0 0 1 18.9 8zM12 4c.8 1.2 1.5 2.5 1.9 4h-3.8c.4-1.5 1.1-2.8 1.9-4zM4.3 14a8 8 0 0 1 0-4h3.4a16 16 0 0 0 0 4zm.8 2h3a15 15 0 0 0 1.3 3.6A8 8 0 0 1 5.1 16zm3-8h-3a8 8 0 0 1 4.3-3.6C8.8 5.5 8.4 6.7 8.1 8zM12 20c-.8-1.2-1.5-2.5-1.9-4h3.8c-.4 1.5-1.1 2.8-1.9 4zm2.3-6H9.7a14 14 0 0 1 0-4h4.6a14 14 0 0 1 0 4zm.3 5.6c.6-1.1 1-2.3 1.3-3.6h3a8 8 0 0 1-4.3 3.6zm1.7-5.6a16 16 0 0 0 0-4h3.4a8 8 0 0 1 0 4z"/></svg></li>
      <li class="contact__item">Street address goes here,
        <svg class="icon" viewBox="0 0 24 24"><path d="M12 3 2 12h3v8h5v-5h4v5h5v-8h3z"/></svg></li>
      <li class="contact__item">Suite #303, Alt Bldg, NY 82365
        <svg class="icon icon--blank" viewBox="0 0 24 24"></svg></li>
    </ul>
  </div>
</section>

</body>
</html>
```